Packiging of mouse trap

We need a packiging for a new mousetrap called 'The Snapwell'. It is a mouse/rat trap. We want to have it pretty simple and modern. The logo of the mouse trap is in the attachment and the measures of the packaging also (don't look at the design, it has nothing to do with us). It's needs to stand out in between the other packaging due to it's simplicity and modern touch.

Font styles to use
Sans Serif

Requirements
Must have
• Simplicity, modern
Should not have
• Too many colors

```html
<!DOCTYPE html>
<html lang="en">
<head>
<meta charset="utf-8">
<title>The Snapwell – Mouse/Rat Trap Packaging</title>
<link href="https://fonts.googleapis.com/css2?family=Saira:wght@400;800&display=swap" rel="stylesheet">
<style>
  :root {
    --backdrop: #dcd8d9;
    --panel-black: #0b0b0b;
    --smoke-grey: #2a2a2a;
    --label-white: #ffffff;
    --label-shade: #d9d9d9;
    --rule-grey: #9a9a9a;
    --ink: #1a1a1a;
  }
  * { margin: 0; padding: 0; box-sizing: border-box; }
  html, body {
    width: 1200px; height: 1200px; overflow: hidden;
    background: var(--backdrop);
    font-family: "Saira", sans-serif;
  }
  .package {
    position: absolute; left: 310px; top: 80px;
    display: flex; height: 1040px;
  }
  .panel { position: relative; height: 100%; overflow: hidden; }
  .panel-side {
    width: 160px;
    background: linear-gradient(90deg, #050505, #141414);
    border-right: 1px solid #2b2b2b;
  }
  .panel-front {
    width: 420px;
    background: var(--panel-black);
  }
  .smoke-texture {
    position: absolute; inset: 0;
    background:
      radial-gradient(ellipse 60% 40% at 70% 35%, rgba(90,90,90,0.35), transparent 70%),
      radial-gradient(ellipse 50% 30% at 30% 60%, rgba(70,70,70,0.3), transparent 70%),
      linear-gradient(180deg, #141414, var(--panel-black) 60%, var(--smoke-grey));
  }
  .wordmark {
    position: absolute; left: 0; right: 0;
    color: var(--label-white);
    font-weight: 800; text-transform: uppercase;
    text-align: center; line-height: 0.88;
    letter-spacing: -0.02em;
  }
  .panel-front .wordmark { top: 330px; font-size: 58px; }
  .panel-side .wordmark { top: 410px; font-size: 26px; }
  .side-details {
    position: absolute; left: 10px; bottom: 14px;
    color: var(--label-white);
    font-size: 8px; line-height: 1.25; font-weight: 400;
  }
  .side-details strong { font-weight: 800; }
  .product-label {
    position: absolute; left: 0; right: 0; bottom: 0; height: 250px;
    background: linear-gradient(180deg, var(--label-white) 0%, #f1f1f1 55%, var(--label-shade) 100%);
    border-top: 4px solid var(--rule-grey);
    display: flex; align-items: center; justify-content: center;
  }
  .product-name {
    color: var(--ink);
    font-size: 34px; font-weight: 400; letter-spacing: 0.06em;
    text-align: center; line-height: 1.15;
    margin-top: 10px;
  }
</style>
</head>
<body>
  <main class="package">
    <section class="panel panel-side">
      <div class="smoke-texture" role="img" aria-label="Dark smoke texture background"></div>
      <p class="wordmark">The<br>Snapwell</p>
      <p class="side-details">
        <strong>THE SNAPWELL</strong><br>
        Electronic Rat Trap<br>
        www.snapwell-home.com<br>
        Model No.: 000000<br>
        Est.No : 000.0000-0000
      </p>
    </section>
    <section class="panel panel-front">
      <div class="smoke-texture" role="img" aria-label="Dark smoke texture background"></div>
      <p class="wordmark">The<br>Snapwell</p>
      <div class="product-label">
        <p class="product-name">MOUSE/RAT<br>TRAP</p>
      </div>
    </section>
  </main>
</body>
</html>
```